Hydroponic Farm Needs a Business Card

We need a business card design for a hydroponic farm located on the Gulf Coast called 'Tallowbend Farms'. We grow many forms of lettuce and tomatoes along with other herbs and spices. We currently sell to farmer's markets though will soon be expanding to commercial accounts such as restaurants and grocery stores. The colors should be bright and vibrant to reflect the nature of our produce. The final design should communicate a professional, clean, yet friendly impression and able to be used both with farmer's markets and commercial accounts.

The pictures are an example of our product. The pictures do not have to be incorporated into the business card design.

Please put areas for information such as Names, Phone Number, E-mail address, and additional information.

Industry/Entity Type

Farm

```html
<!DOCTYPE html>
<html lang="en">
<head>
<meta charset="utf-8">
<title>Tallowbend Farms – Business Card</title>
<link rel="stylesheet" href="https://fonts.googleapis.com/css2?family=Bebas+Neue&family=Oswald:wght@700&family=Arimo:wght@400&family=Roboto:wght@300&family=Dosis:wght@500&display=swap">
<style>
  :root {
    --card-green: #99ff00;
    --ink-dark: #2a1420;
    --white: #ffffff;
    --faint-text: #c9ff66;
    --leaf: #3aa02a;
  }
  html, body {
    margin: 0;
    padding: 0;
    overflow: hidden;
    background: var(--card-green);
  }
  .card {
    position: relative;
    width: 1200px;
    height: 686px;
    background: var(--card-green);
    overflow: hidden;
  }
  .brand {
    position: absolute;
    right: 89px;
    top: 56px;
    text-align: right;
  }
  .brand-name {
    font-family: "Oswald", sans-serif;
    font-weight: 700;
    font-size: 44px;
    line-height: 48px;
    letter-spacing: 1px;
    color: var(--ink-dark);
    margin: 0;
  }
  .brand-tagline {
    display: flex;
    align-items: center;
    justify-content: flex-end;
    gap: 20px;
    margin-top: 2px;
  }
  .brand-dot {
    width: 22px;
    height: 22px;
    border-radius: 50%;
    background: var(--leaf);
  }
  .brand-sub {
    font-family: "Arimo", sans-serif;
    font-size: 34px;
    line-height: 36px;
    letter-spacing: 1px;
    color: var(--white);
  }
  .divider {
    position: absolute;
    left: 617px;
    top: 172px;
    width: 494px;
    height: 2px;
    background: var(--ink-dark);
  }
  .fact {
    position: absolute;
    left: 837px;
    top: 196px;
    width: 280px;
    font-family: "Roboto", sans-serif;
    font-weight: 300;
    font-size: 16px;
    line-height: 18.3px;
    color: var(--faint-text);
  }
  .fact p { margin: 0 0 8px; }
  .fact-source {
    text-align: right;
    width: 274px;
    margin-top: 14px !important;
  }
  .person {
    position: absolute;
    left: 86px;
    top: 262px;
  }
  .person-name {
    font-family: "Bebas Neue", sans-serif;
    font-size: 56px;
    line-height: 54px;
    letter-spacing: 3px;
    color: var(--white);
    margin: 0;
  }
  .person-role {
    font-family: "Bebas Neue", sans-serif;
    font-size: 32px;
    line-height: 32px;
    letter-spacing: 0.5px;
    color: var(--ink-dark);
    margin: 0;
  }
  .contact {
    position: absolute;
    left: 86px;
    font-family: "Dosis", sans-serif;
    font-weight: 500;
    font-size: 28px;
    color: var(--ink-dark);
    margin: 0;
  }
  .contact-phone { top: 422px; }
  .contact-list {
    top: 512px;
    list-style: none;
    padding: 0;
    line-height: 36px;
  }
  .contact-list li:last-child { margin-top: 4px; }
</style>
</head>
<body>
<main class="card">
  <header class="brand">
    <h1 class="brand-name">TALLOWBEND FARMS</h1>
    <div class="brand-tagline">
      <span class="brand-dot"></span>
      <span class="brand-sub">HYDROPHONICS</span>
    </div>
  </header>

  <div class="divider"></div>

  <aside class="fact">
    <p>Are Hyprophonic Vegetables Healthy?</p>
    <p>In general, the nutritional value<br>of hydrophonically grown vegetables<br>is about the same as that of<br>conventionally grown produce.</p>
    <p>Consuming a diet high in vegetables<br>can improve your health, no matter<br>whether the vegetables were<br>conventionally or hydrophonically<br>grown.&nbsp; A diet high in vegetables<br>reduces the risk of stroke, type 2<br>diabetes and some cancer.</p>
    <p class="fact-source">greenplatehealth.org</p>
  </aside>

  <section class="person">
    <h2 class="person-name">DALE HARROW</h2>
    <p class="person-role">HYDROPHONICS GROWER</p>
  </section>

  <p class="contact contact-phone">091.555.0142</p>

  <ul class="contact contact-list">
    <li>dale@tallowbendfarms.com</li>
    <li>http://www.tallowbendfarms.com</li>
    <li>Social: @tallowbendfarms</li>
  </ul>
</main>
</body>
</html>
```